Drug safety monitoring company requires a new corporate website

We are an outsourcing partner to large and small companies within the pharmaceutical industry. Our current website www.quorvanta.co.uk has not been updated in a long time. We want a new web site that is responsive and modern but with a clearly corporate and professional feel. We want a design based on a 12 column grid system (mobile and desktop version). We want to use a new, modern font (not the standard web fonts) - we will purchase as required. Content can be used as is from the current website. Red and white are the corporate colours, so a palate should be developed to match. We do not need as much red as is in the current website. New icons (preferably in svg format) would be great. We can also purchase new images from Framly (or other) as required. We would prefer submissions in Sketch if possible.

Target Market(s)

Pharmaceutical companies

Number of Pages Required

1 page

Font styles to use
Sans Serif

Colors
ec1f27
ffffff

Requirements
Must have
• Design based on 12 column grid system.
Responsive design (i.e. require a mobile and desktop version).
How should the menu look between desktop and mobile?
A coherent colour palete.
Content to come from the existing website: www.quorvanta.co.uk
How should links be styled?
How should headings, sub-headings, paragraphs be styled?
Nice to have
• Custom developed icons (these are along the bottom of the page on the existing website: Medical Information; Pharmacovigilance; Literature Monitoring; Training).
New imagery (the images on the current website are dated).
Submission ideally as Sketch files (but we are okay with photoshop too).
A new, modern, non-standard font.
Not so much red in the design.
If we had buttons on the website, how should they be styled?
If we had a form on the website, how should the fields be styled?

```html
<!DOCTYPE html>
<html lang="en">
<head>
<meta charset="utf-8">
<title>Quorvanta Pharmacovigilance</title>
<link href="https://fonts.googleapis.com/css2?family=Montserrat:wght@400;500;600;700&display=swap" rel="stylesheet">
<style>
:root{
  --red:#ec1f27;
  --white:#ffffff;
  --grey-bg:#e6e6e6;
  --nav:#b07a5c;
  --orange-a:#ffae85;
  --orange-b:#f58a5c;
  --yellow:#fbb62b;
  --footer:#d63a3f;
  --text:#555;
  --muted:#777;
  --field:#666;
}
*{margin:0;padding:0;box-sizing:border-box}
html,body{width:802px;height:1200px;overflow:hidden}
body{font-family:'Montserrat',sans-serif;background:var(--grey-bg);position:relative;color:var(--text)}
.abs{position:absolute}
.hero-bg{left:0;top:0;width:802px;height:376px}
.site-nav{left:0;top:0;width:802px;height:36px;background:var(--nav);opacity:.95}
.brand{left:100px;top:8px;width:93px;height:20px;background:var(--white);border-radius:10px;display:flex;align-items:center;justify-content:center;font-weight:600;font-size:10px;letter-spacing:1.5px;color:var(--red)}
.menu a{position:absolute;top:13px;font-size:7px;font-weight:600;color:var(--white);text-decoration:none;white-space:nowrap}
.menu .active::after{content:"";position:absolute;left:0;right:0;top:21px;height:1px;background:var(--red)}
.hero-title{left:100px;top:120px;width:420px;font-size:18.5px;line-height:28.5px;font-weight:500;color:var(--white)}
.hero-title strong{color:var(--red);font-weight:700}
.btn-ghost{left:99px;top:210px;width:75px;height:25px;border:1px solid var(--white);color:var(--white);font-size:7px;display:flex;align-items:center;justify-content:center}
.service{top:326px;width:143px;height:100px;background:var(--white);box-shadow:0 1px 4px rgba(0,0,0,.08)}
.service .icon{position:absolute;left:8px;top:28px;width:47px;height:47px;border-radius:50%}
.service h3{position:absolute;left:63px;top:22px;font-size:7.2px;font-weight:500;color:var(--red);white-space:nowrap}
.service p{position:absolute;left:63px;top:33px;width:76px;font-size:5.6px;line-height:9.5px;color:var(--muted)}
.service a{position:absolute;left:63px;top:73px;font-size:5.8px;font-weight:600;color:var(--red);text-decoration:none}
.about{left:99px;top:496px;width:310px;height:313px;background:var(--white);box-shadow:0 1px 4px rgba(0,0,0,.08);padding:18px 23px}
.about h2{font-size:15.5px;line-height:24px;font-weight:400;color:var(--text)}
.about h2 span{color:var(--red);font-weight:500}
.about p{font-size:7.1px;line-height:11px;color:var(--text);margin-top:11px;letter-spacing:-.1px}
.about h2+p{margin-top:8px}
.photo{left:435px;top:496px;width:266px;height:313px;background:linear-gradient(180deg,#cfc6bd 0%,#a89a8c 40%,#7c8a73 70%,#e9e9ec 100%)}
.help-bg{left:0;top:849px;width:802px;height:326px}
.help-title{left:101px;top:897px;font-size:18.5px;font-weight:600;color:var(--white)}
.help-title span{color:var(--red)}
.help-sub{left:99px;top:933px;width:300px;font-size:9.8px;line-height:16px;color:#6a6a7a}
.faq{left:100px;width:265px;height:37px;background:var(--white);padding:10px 40px 0 10px;font-size:6.2px;line-height:11px;color:var(--text)}
.faq svg{position:absolute;right:12px;top:15px}
.form{left:456px;top:896px;width:246px;height:250px;background:var(--white)}
.form label{position:absolute;font-size:5.2px;color:var(--field)}
.form .field{position:absolute;border:1px solid #888;border-radius:1px}
.btn-submit{left:87px;top:205px;width:75px;height:24px;background:var(--red);color:var(--white);font-size:7px;font-weight:700;display:flex;align-items:center;justify-content:center}
.site-footer{left:0;top:1175px;width:802px;height:25px;background:var(--footer);color:var(--white);font-size:6.2px}
.site-footer span{position:absolute;top:9px;white-space:nowrap}
</style>
</head>
<body>

<svg class="abs hero-bg" role="img" aria-label="Orange and white capsules spilling from a pill bottle on an orange surface" viewBox="0 0 802 376">
  <defs>
    <linearGradient id="heroGrad" x1="0" y1="0" x2="1" y2="1">
      <stop offset="0" stop-color="#ffb48d"/>
      <stop offset=".6" stop-color="#fb9d72"/>
      <stop offset="1" stop-color="#f38556"/>
    </linearGradient>
  </defs>
  <polygon points="0,0 802,0 802,230 0,376" fill="url(#heroGrad)"/>
</svg>

<div class="abs site-nav"></div>
<div class="abs brand">QUORVANTA</div>
<nav class="menu">
  <a class="active" style="left:420px">HOME</a>
  <a style="left:457px">ABOUT US</a>
  <a style="left:509px">QPPV</a>
  <a style="left:543px">OUR SERVICES</a>
  <a style="left:613px">CON TACT US</a>
  <a style="left:675px">CLIENT</a>
</nav>

<h1 class="abs hero-title">At Quorvanta we ensure that your business has the best <strong>Pharmacovigilance support</strong> in the industry</h1>
<div class="abs btn-ghost">Learn More</div>

<div class="abs service" style="left:100px">
  <div class="icon" role="img" aria-label="Prescription document icon" style="background:linear-gradient(135deg,#a05bd6,#7b3fb8)"></div>
  <h3>Medical Information</h3>
  <p>Professional enquiry handling to support the safe and effective use of your products.</p>
  <a>Learn More</a>
</div>
<div class="abs service" style="left:253px">
  <div class="icon" role="img" aria-label="Eye icon" style="background:linear-gradient(135deg,#f9a23a,#e9782b)"></div>
  <h3>Pharmacovigilance</h3>
  <p>Ease the regulatory burden, keep compliant with current pharmaco-vigilance legislation.</p>
  <a>Learn More</a>
</div>
<div class="abs service" style="left:406px">
  <div class="icon" role="img" aria-label="Clipboard report icon" style="background:linear-gradient(135deg,#fbe37a,#f3c53b)"></div>
  <h3 style="left:60px">Literature Monitoring</h3>
  <p style="left:61px">Product safety montiored through surveillance of published articles and case reports.</p>
  <a style="left:61px">Learn More</a>
</div>
<div class="abs service" style="left:559px">
  <div class="icon" role="img" aria-label="Medical staff icon" style="left:16px;background:linear-gradient(135deg,#9b5bd4,#6c3aa8)"></div>
  <h3 style="left:70px">Training</h3>
  <p style="left:70px;width:66px">Confident staff to support the pharmacovigilance process.</p>
  <a style="left:70px">Learn More</a>
</div>

<section class="abs about">
  <h2><span>Pharmacovigilance</span> outsourcing to support your product portfolio</h2>
  <p>Welcome to the Quorvanta Pharmacovigilance website. We are an outsourcing partner to large and small companies within the pharmaceutical industry. Our range of services is tailored to suit each of our client’s needs and cover both human and veterinary medicinal products.</p>
  <p>Pharmacovigilance is defined by WHO as ‘The science and activities relating to the detection, assessment, understanding and prevention of adverse effects or any other drug-related problems’. The process is one of managing risk associated with medicinal products, in an effort to promote their safe and effective use by prescribers and patients.</p>
  <p>Our primary functions are EU QPPV and related pharmacovigilance services to assist and support Marketing Authorisation Holders (MAH), of pharmaceutical product licences, in their efforts to remain compliant with EU regulatory requirements (Regulation 1235/2010 and Directive 2010/84/EU) the deadline for which implementing ended on 21 July 2012.</p>
  <p>The regulatory environment is an ever-changing and evolving one. Legislation is global and the management of this process is complex, requiring a strong relationship between Marketing Authorisation Holders and their QPPV.</p>
</section>
<div class="abs photo" role="img" aria-label="Doctor in a white coat wearing a surgical mask and stethoscope, outdoors"></div>

<svg class="abs help-bg" role="img" aria-label="Yellow surface with scattered capsules and medical items" viewBox="0 0 802 326">
  <polygon points="0,0 802,146 802,326 0,326" fill="#fbb62b"/>
</svg>

<h2 class="abs help-title"><span>How Can</span> We Help?</h2>
<p class="abs help-sub">You can browse through our FAQ’s to see solutions for popular queries or fill out our contact form</p>

<div class="abs faq" style="top:976px">Lorem ipsum dolor sit amet, consectetur adipiscing elit. dolor sit ame Nam in mi id.?<svg width="8" height="5" viewBox="0 0 8 5"><path d="M0.5 0.5 4 4 7.5 0.5" fill="none" stroke="#777" stroke-width=".8"/></svg></div>
<div class="abs faq" style="top:1018px">Lorem ipsum dolor sit amet, consectetur adipiscing elit. dolor sit ame Nam in mi id.?<svg width="8" height="5" viewBox="0 0 8 5"><path d="M0.5 0.5 4 4 7.5 0.5" fill="none" stroke="#777" stroke-width=".8"/></svg></div>
<div class="abs faq" style="top:1061px">Lorem ipsum dolor sit amet, consectetur adipiscing elit. dolor sit ame Nam in mi id.?<svg width="8" height="5" viewBox="0 0 8 5"><path d="M0.5 0.5 4 4 7.5 0.5" fill="none" stroke="#777" stroke-width=".8"/></svg></div>
<div class="abs faq" style="top:1104px">Lorem ipsum dolor sit amet, consectetur adipiscing elit. dolor sit ame Nam in mi id.?<svg width="8" height="5" viewBox="0 0 8 5"><path d="M0.5 0.5 4 4 7.5 0.5" fill="none" stroke="#777" stroke-width=".8"/></svg></div>

<form class="abs form">
  <label style="left:19px;top:22px">First Name</label>
  <div class="field" style="left:19px;top:32px;width:100px;height:20px"></div>
  <label style="left:125px;top:22px">Last Name</label>
  <div class="field" style="left:125px;top:32px;width:100px;height:20px"></div>
  <label style="left:19px;top:61px">Mobile Number</label>
  <div class="field" style="left:19px;top:71px;width:206px;height:20px"></div>
  <label style="left:19px;top:100px">Email Address</label>
  <div class="field" style="left:19px;top:110px;width:206px;height:20px"></div>
  <label style="left:19px;top:139px">Message</label>
  <div class="field" style="left:19px;top:149px;width:206px;height:45px"></div>
  <div class="abs btn-submit">SUBMIT</div>
</form>

<footer class="abs site-footer">
  <span style="left:99px">Mets</span>
  <span style="left:260px">Contact us - 0330 4471 208</span>
  <span style="right:101px">Copyright © 2020 Quorvanta Ltd (Registered in England &amp; Wales : 07284416)</span>
</footer>

</body>
</html>
```